Vel Tor Concrete Post Card Design Project

Hello, We are A Concrete Contractor. We specialize in removing and replacing concrete walkways, Patio's, Driveway's, ect., that are a trip hazard. We work a lot in Apartment complexes and Business Complexes where the trees have grown big and the roots from the trees lift up the concrete.
I would like someone to design a postcard (Two Sided) so I can send it out and market potential property manager customers. I would like to use our company logo on this card. Please see the snap vault link below. Here are some things I would like the card to have on it.

1.Removal and Replacement of Concrete Sidewalks, Driveways, Parking Lots, Curb and Gutter.

2. ADA Compliant.

3. Repair of concrete tripping hazards and
root-damaged sidewalks.

4. Vel Tor Concrete brings your sidewalks in compliance with the Americans With Disabilities Act (ADA).

5. Property Management:

We cater to the needs of Property Mangement Companies, HOA, Apartment Complexes, Business Parks, Senior Living Complexes, Government Buildings and Shopping Centers.

6. Free Estimates
7. Contractors license number under our logo. It is:
RBQC #318907
8. Our phone numbers:530-842-1964 and 530-729-6350.

Card should be two sided 9" by 6"

Thank You
Updates

This website would not let me upload my logo so please click on the link below to get it.

 

http://img4471.snapvaultpix.net/albums/k302/Jvelt42/VelTorConcreteLogo-2012-PROOF-2.jpg

Thank You

Reason: Hello, I have a lot of great designs. I have had a busy week and I am just now sitting down to ask for the changes I would like. Once I recieve all of the designs back with the changes I requested I would like to get the opinions of my coworkers and friends before selecting the design. I am asking for the deadline to be extended by 4 days. Thank You so much, Janice Vel Tor

Target Market(s)

Property Managers

Industry/Entity Type

Concrete

Requirements
Must have
• Our logo

```html
<!DOCTYPE html>
<html lang="en">
<head>
<meta charset="utf-8">
<title>Vel Tor Concrete – Postcard</title>
<link href="https://fonts.googleapis.com/css2?family=Arimo:wght@400;700&family=Questrial&display=swap" rel="stylesheet">
<style>
  :root {
    --stage: #3a3a3a;
    --silver-light: #f1f1f1;
    --silver-mid: #cfcfcf;
    --silver-dark: #a9a9a9;
    --ink: #111111;
    --band: #1b1b1b;
    --band-edge: #4a4a4a;
    --white: #ffffff;
  }
  * { box-sizing: border-box; margin: 0; padding: 0; }
  html, body { width: 1200px; height: 900px; overflow: hidden; }
  body {
    position: relative;
    background: var(--stage);
    font-family: "Arimo", Arial, sans-serif;
    color: var(--ink);
  }
  .presentation-title {
    position: absolute;
    top: 34px;
    right: 44px;
    font-family: "Questrial", sans-serif;
    font-size: 50px;
    font-weight: 400;
    color: var(--white);
    letter-spacing: 0.5px;
  }
  /* 9 x 6 postcard proportion */
  .card {
    position: absolute;
    width: 540px;
    height: 360px;
    overflow: hidden;
    background: linear-gradient(135deg, var(--silver-light) 0%, var(--silver-mid) 45%, var(--silver-light) 70%, var(--silver-dark) 100%);
    box-shadow: 0 10px 26px rgba(0,0,0,.55);
  }
  /* Back side: services */
  .card--back { left: 40px; top: 110px; }
  .card--back .edge-shape { position: absolute; inset: 0; width: 100%; height: 100%; }
  .services {
    position: absolute;
    left: 30px;
    top: 28px;
    width: 420px;
    font-size: 14px;
    line-height: 1.25;
  }
  .services h2 {
    font-size: 14.5px;
    font-weight: 700;
    margin-bottom: 14px;
  }
  .services h3 {
    font-size: 15px;
    font-weight: 700;
  }
  .services p { margin-bottom: 14px; }
  .website {
    position: absolute;
    right: 50px;
    bottom: 14px;
    font-size: 17px;
    color: var(--white);
  }
  /* Front side: contact */
  .card--front { left: 620px; top: 480px; }
  .band {
    position: absolute;
    left: 0; right: 0;
    height: 22px;
    background: linear-gradient(180deg, var(--band-edge), var(--band));
  }
  .band--top { top: 0; }
  .band--bottom { bottom: 0; }
  .brand {
    position: absolute;
    left: 32px;
    top: 150px;
  }
  .brand-name {
    display: flex;
    align-items: center;
    gap: 9px;
    font-size: 22px;
    font-weight: 700;
  }
  .brand-dot { width: 13px; height: 13px; border-radius: 50%; background: var(--ink); }
  .license {
    margin-top: 8px;
    padding-left: 22px;
    font-size: 14px;
    font-weight: 700;
  }
  .free-estimates {
    position: absolute;
    left: 32px;
    bottom: 40px;
    font-size: 18px;
    font-weight: 700;
  }
  .contact {
    position: absolute;
    left: 272px;
    top: 58px;
    font-size: 16px;
    line-height: 1.15;
  }
  .contact-name { font-size: 19px; font-weight: 700; }
  .contact-role { font-size: 14px; font-weight: 700; margin-bottom: 20px; }
  .contact-email { margin-bottom: 18px; }
  .contact-address { margin-bottom: 18px; }
  .contact-phones b { display: inline-block; width: 16px; }
</style>
</head>
<body>
  <h1 class="presentation-title">Vel Tor Concrete</h1>

  <section class="card card--back" aria-label="Postcard back: services">
    <svg class="edge-shape" viewBox="0 0 540 360" preserveAspectRatio="none" aria-hidden="true">
      <defs>
        <linearGradient id="edgeDark" x1="0" y1="0" x2="1" y2="1">
          <stop offset="0" stop-color="#2a2a2a"/>
          <stop offset="1" stop-color="#0d0d0d"/>
        </linearGradient>
        <linearGradient id="edgeGrey" x1="0" y1="0" x2="1" y2="0">
          <stop offset="0" stop-color="#b9b9b9"/>
          <stop offset="1" stop-color="#6f6f6f"/>
        </linearGradient>
      </defs>
      <polygon points="470,0 540,0 540,360 505,360" fill="url(#edgeDark)"/>
      <polygon points="0,360 0,326 470,298 505,360" fill="url(#edgeGrey)"/>
      <polygon points="470,0 505,360 470,298" fill="#8a8a8a"/>
    </svg>
    <div class="services">
      <h2>Removal and Replacement of Concrete Sidewalks, Driveways, Parking Lots, Curb and Gutters and ADA Compliant</h2>
      <h3>Concrete Grinding:</h3>
      <p>Repair of tripping hazard removal, Root-damaged sidewalks, 24 Hr Service. <b>Vel Tor Concrete</b> brings your sidewalks in compliance with the Americans With Disabilities Act (ADA).</p>
      <h3>Property Management:</h3>
      <p>We cater to the needs of Property Mangement Companies, HOA, Apartment Complexes, Business Parks, Senior Living Complex, Government Buildings and Shopping Centers, Concrete trip hazard repair and removal, Sidewalk concrete repair.</p>
    </div>
    <span class="website">www.veltorconcrete.com</span>
  </section>

  <section class="card card--front" aria-label="Postcard front: contact">
    <div class="band band--top"></div>
    <div class="brand">
      <div class="brand-name"><span class="brand-dot"></span>Vel Tor Concrete</div>
      <div class="license">RBQC #318907</div>
    </div>
    <div class="free-estimates">Free Estimates</div>
    <div class="contact">
      <div class="contact-name">Carl Brennick</div>
      <div class="contact-role">President</div>
      <div class="contact-email">cbrennick@veltorconcrete.com</div>
      <div class="contact-address">4417 Marrow Creek Road #118<br>Redding, CA 96002</div>
      <div class="contact-phones">
        <div><b>P</b> (530) 842-1964</div>
        <div><b>F</b> (530) 842-1975</div>
        <div><b>M</b> (530) 729-6350</div>
      </div>
    </div>
    <div class="band band--bottom"></div>
  </section>
</body>
</html>
```